'Our Values' graphic

Hi there,
Could I get few options creating this graphic in a more minimalist, corporate look - using minimalist graphic elements and designs and using minimalist fonts (see tavlix or mundelo for inspiration)
I would also like the lines around the outside to be more minimalist. Maybe a thin line or a graphic element.
Change 'Core Values' title to 'Our Values'
Keep the font of 'Values'.
I would like to see a version in all dark grey and another version with the font in the lower square with each line of font being a different colour (Red, Blue, Green and Orange)

Requirements
Must have
• 'Our Values' and using the same font for 'Values' as the original artwork
Nice to have
• Minimalist artwork

```html
<!DOCTYPE html>
<html lang="en">
<head>
<meta charset="UTF-8">
<title>Our Values</title>
<link rel="stylesheet" href="https://fonts.googleapis.com/css2?family=Caveat+Brush&family=Permanent+Marker&family=Poppins:wght@800&display=swap">
<style>
  :root {
    --backdrop: #eceef0;
    --card: #ffffff;
    --ink: #1c1c1c;
    --charcoal: #3a3a3a;
    --bar: #bababa;
    --ring-shade: #7a7a7a;
    --white: #ffffff;
  }
  * { margin: 0; padding: 0; box-sizing: border-box; }
  html, body {
    width: 1096px;
    height: 1200px;
    overflow: hidden;
    background: var(--backdrop);
  }
  .values-card {
    position: absolute;
    left: 111px;
    top: 108px;
    width: 874px;
    height: 984px;
    background: var(--card);
  }
  .title-box {
    position: absolute;
    left: 140px;
    top: 137px;
    width: 816px;
    height: 262px;
    border: 1.5px solid var(--charcoal);
    border-radius: 14px;
    overflow: hidden;
    display: flex;
  }
  .title-our {
    width: 378px;
    display: flex;
    align-items: center;
    justify-content: center;
    font-family: "Permanent Marker", cursive;
    font-size: 160px;
    line-height: 1;
    color: var(--ink);
    padding-top: 14px;
    padding-left: 14px;
  }
  .title-values {
    flex: 1;
    background: var(--charcoal);
    display: flex;
    align-items: center;
    justify-content: center;
    font-family: "Caveat Brush", cursive;
    font-size: 190px;
    line-height: 1;
    color: var(--white);
    padding-bottom: 6px;
  }
  .value-bar {
    position: absolute;
    left: 197px;
    width: 759px;
    height: 103px;
    background: var(--bar);
    border-radius: 14px;
    display: flex;
    align-items: center;
    padding-left: 90px;
    font-family: "Poppins", sans-serif;
    font-weight: 800;
    font-size: 44px;
    letter-spacing: -0.5px;
    color: var(--ink);
  }
  .bar-rise { top: 465px; }
  .bar-innovate { top: 614px; }
  .bar-safety { top: 765px; }
  .bar-empower { top: 914px; }
  .acronym-chain {
    position: absolute;
    left: 0;
    top: 0;
  }
  .chain-letter {
    font-family: "Poppins", sans-serif;
    font-weight: 800;
    font-size: 40px;
    fill: var(--ink);
  }
</style>
</head>
<body>
  <div class="values-card"></div>

  <header class="title-box">
    <div class="title-our">OUR</div>
    <div class="title-values">Values</div>
  </header>

  <div class="value-bar bar-rise">RISE TOGETHER</div>
  <div class="value-bar bar-innovate">INNOVATE EDUCATION</div>
  <div class="value-bar bar-safety">SAFETY FIRST</div>
  <div class="value-bar bar-empower">EMPOWER CONNECTIONS</div>

  <svg class="acronym-chain" width="1096" height="1200" viewBox="0 0 1096 1200" aria-hidden="true">
    <g fill="var(--charcoal)">
      <path d="M186 568 Q196 590 195 606 L203 606 Q202 590 212 568 Z"/>
      <path d="M186 714 Q196 738 195 758 L203 758 Q202 738 212 714 Z"/>
      <path d="M186 866 Q196 890 195 913 L203 913 Q202 890 212 866 Z"/>
    </g>
    <g fill="var(--ring-shade)">
      <circle cx="203" cy="517" r="55"/>
      <circle cx="203" cy="663" r="55"/>
      <circle cx="203" cy="815" r="55"/>
      <circle cx="203" cy="968" r="55"/>
    </g>
    <g fill="var(--charcoal)">
      <circle cx="199" cy="517" r="55"/>
      <circle cx="199" cy="663" r="55"/>
      <circle cx="199" cy="815" r="55"/>
      <circle cx="199" cy="968" r="55"/>
      <circle cx="199" cy="606" r="6"/>
      <circle cx="199" cy="758" r="6"/>
      <circle cx="199" cy="913" r="6"/>
    </g>
    <g fill="var(--white)">
      <circle cx="199" cy="517" r="42"/>
      <circle cx="199" cy="663" r="42"/>
      <circle cx="199" cy="815" r="42"/>
      <circle cx="199" cy="968" r="42"/>
    </g>
    <g text-anchor="middle">
      <text class="chain-letter" x="199" y="531">R</text>
      <text class="chain-letter" x="199" y="677">I</text>
      <text class="chain-letter" x="199" y="829">S</text>
      <text class="chain-letter" x="199" y="982">E</text>
    </g>
  </svg>
</body>
</html>
```